POLITICAL CARD TO HAND OUT

A LITTLE LARGER THAN THE REGULAR BUSINESS CARD WITH THE ABOVE INFORMATION.

Industry/Entity Type

Business

Contact Information for Business Card

ELECT *DEAN HOLT* FOR JUSTICE OF THE PEACE PCT 6-EXPERIENCED LEADERSHIP- WITH MY PICTURE ON IT- PHONE 347-610-2853-MERIDIAN PRIMARY - EARLY VOTING FEB 18TH THRU FEB 28 AND ELECTION DAY IS MARCH 4TH, 2014- USE RED WHITE AND BLUE WITH SOME STARS.

Requirements
Must have
• A FIVE POINTED STAR ON EACH SIDE OF MY NAME

```html
<!DOCTYPE html>
<html lang="en">
<head>
<meta charset="utf-8">
<title>Elect Dean Holt for Justice of the Peace</title>
<link rel="stylesheet" href="https://fonts.googleapis.com/css2?family=Libre+Franklin:ital,wght@0,700;0,800;0,900;1,800;1,900&display=swap">
<style>
  :root {
    --card-blue: #3d55a7;
    --card-red: #ea1c24;
    --card-white: #ffffff;
    --photo-light: #f1eeec;
    --photo-mid: #d9d3cf;
    --photo-dark: #1e1b1c;
  }
  html, body {
    margin: 0;
    padding: 0;
    width: 1200px;
    height: 702px;
    overflow: hidden;
    background: var(--card-white);
  }
  .campaign-card {
    display: block;
    width: 1200px;
    height: 702px;
    font-family: "Libre Franklin", "Arial Black", sans-serif;
  }
  .name-panel { fill: var(--card-blue); }
  .info-band { fill: var(--card-red); }
  .card-text { fill: var(--card-white); }
  .name-star { fill: var(--card-white); }
  .elect-call { font-style: italic; font-weight: 900; font-size: 50px; }
  .candidate-name { font-weight: 900; font-size: 104px; }
  .for-word { font-weight: 800; font-size: 40px; }
  .office-title { font-weight: 800; font-size: 72px; }
  .tagline { font-weight: 800; font-size: 37px; }
  .band-line { font-weight: 800; font-size: 30px; }
</style>
</head>
<body>
<svg class="campaign-card" viewBox="0 0 1200 702" xmlns="http://www.w3.org/2000/svg">
  <defs>
    <linearGradient id="portrait-tone" x1="0" y1="0" x2="0" y2="1">
      <stop offset="0" stop-color="var(--photo-light)"/>
      <stop offset="0.45" stop-color="var(--photo-mid)"/>
      <stop offset="0.6" stop-color="#3a3435"/>
      <stop offset="1" stop-color="var(--photo-dark)"/>
    </linearGradient>
    <path id="five-point-star" d="M0,-30 L6.7,-9.3 L28.5,-9.3 L10.9,3.5 L17.6,24.3 L0,11.5 L-17.6,24.3 L-10.9,3.5 L-28.5,-9.3 L-6.7,-9.3 Z"/>
  </defs>

  <rect class="name-panel" x="59" y="56" width="756" height="419"/>
  <rect class="portrait-slot" x="815" y="56" width="326" height="419" fill="url(#portrait-tone)"
        role="img" aria-label="Portrait of the candidate in a white cowboy hat, dark suit and patterned tie"/>
  <rect class="info-band" x="59" y="475" width="1082" height="169"/>

  <text class="card-text elect-call" x="86" y="186" transform="rotate(-16 86 186)">ELECT!</text>

  <use class="name-star" href="#five-point-star" x="132" y="236"/>
  <text class="card-text candidate-name" x="173" y="271" textLength="534" lengthAdjust="spacingAndGlyphs">DEAN HOLT</text>
  <use class="name-star" href="#five-point-star" x="750" y="236"/>

  <text class="card-text for-word" x="190" y="326">FOR</text>
  <text class="card-text office-title" x="88" y="398" textLength="711" lengthAdjust="spacingAndGlyphs">JUSTICE OF THE PEACE</text>
  <text class="card-text tagline" x="155" y="453" textLength="580" lengthAdjust="spacingAndGlyphs">PCT 6-EXPERIENCED LEADERSHIP</text>

  <text class="card-text band-line" x="770" y="512" textLength="357" lengthAdjust="spacingAndGlyphs">PHONE 347-610-2853</text>
  <text class="card-text band-line" x="770" y="550">MERIDIAN PRIMARY</text>
  <text class="card-text band-line" x="77" y="586" textLength="492" lengthAdjust="spacingAndGlyphs">EARLY VOTING FEB 18 TO FEB 28</text>
  <text class="card-text band-line" x="77" y="624" textLength="564" lengthAdjust="spacingAndGlyphs">ELECTION DAY IS MARCH 4TH, 2014</text>
</svg>
</body>
</html>
```